Watch brand needs new business cards

Kestrel Timepiece Company are looking for a new business card design incorporating our logo and brand colours as per our website.

Design should be 90x55mm with 3mm print margin from edges and 3mm external bleed.

Card should be double sided, e.g. logo one side, personal details on the other.

Logo will be provided as a vector.

The card must be able to show:
- Staff name
- Position
- Office Address
- Email
- Telephone number
- Website address

Final work must be provided in an editable format to allow us to add staff details (e.g. an AI or PSD file).

```html
<!DOCTYPE html>
<html lang="en">
<head>
<meta charset="utf-8">
<title>Kestrel Timepiece Company – Business Cards</title>
<link rel="stylesheet" href="https://fonts.googleapis.com/css2?family=Cinzel:wght@600&family=Oswald:wght@500&family=Open+Sans:wght@400&display=swap">
<style>
  :root {
    --backdrop: #3a3a3a;
    --card-dark: #050505;
    --card-dark-sheen: #1f1f1f;
    --card-light: #ffffff;
    --silver: #c9c9c9;
    --ink: #111111;
    --muted: #8a8a8a;
    --divider: #222222;
  }
  * { margin: 0; padding: 0; box-sizing: border-box; }
  html, body {
    width: 1200px;
    height: 1000px;
    overflow: hidden;
    background: var(--backdrop);
  }
  .canvas {
    position: relative;
    width: 1200px;
    height: 1000px;
  }
  .card {
    position: absolute;
    left: 220px;
    width: 760px;
    box-shadow: 0 4px 14px rgba(0,0,0,0.45);
  }
  .card--front {
    top: 50px;
    height: 433px;
    background: linear-gradient(118deg, var(--card-dark) 0%, var(--card-dark) 55%, var(--card-dark-sheen) 62%, #0d0d0d 100%);
  }
  .brand-mark {
    position: absolute;
    left: 50%;
    top: 95px;
    width: 116px;
    height: 116px;
    margin-left: -58px;
    border: 5px solid var(--silver);
    border-radius: 50%;
  }
  .brand-name {
    position: absolute;
    left: 0;
    right: 0;
    top: 248px;
    text-align: center;
    font-family: "Cinzel", serif;
    font-weight: 600;
    font-size: 42px;
    letter-spacing: 2px;
    color: var(--silver);
  }
  .card--back {
    top: 524px;
    height: 435px;
    background: var(--card-light);
  }
  .identity {
    position: absolute;
    right: 414px;
    top: 184px;
    text-align: right;
  }
  .identity__name {
    font-family: "Oswald", sans-serif;
    font-weight: 500;
    font-size: 36px;
    line-height: 1;
    color: var(--ink);
    letter-spacing: 0.3px;
  }
  .identity__role {
    margin-top: 6px;
    font-family: "Open Sans", sans-serif;
    font-size: 16px;
    color: var(--muted);
  }
  .divider {
    position: absolute;
    left: 366px;
    top: 188px;
    width: 2px;
    height: 58px;
    background: var(--divider);
  }
  .contact-list {
    position: absolute;
    left: 388px;
    top: 184px;
    list-style: none;
    font-family: "Open Sans", sans-serif;
    font-size: 16px;
    line-height: 21px;
    color: var(--muted);
  }
  .contact-list li { display: flex; align-items: center; gap: 4px; }
  .contact-list svg { width: 13px; height: 13px; fill: var(--ink); flex: none; }
  .address {
    position: absolute;
    left: 0;
    right: 0;
    top: 382px;
    text-align: center;
    font-family: "Open Sans", sans-serif;
    font-size: 16px;
    color: var(--muted);
  }
  .address__label { color: var(--ink); }
</style>
</head>
<body>
<main class="canvas">
  <section class="card card--front" aria-label="Card front">
    <div class="brand-mark" aria-hidden="true"></div>
    <h1 class="brand-name">Kestrel Timepiece Company</h1>
  </section>

  <section class="card card--back" aria-label="Card back">
    <div class="identity">
      <p class="identity__name">OLIVER HART</p>
      <p class="identity__role">Founder &amp; CEO</p>
    </div>
    <div class="divider"></div>
    <ul class="contact-list">
      <li>
        <svg viewBox="0 0 16 16" aria-hidden="true"><path d="M4 1l3 3-2 2c1 2 3 4 5 5l2-2 3 3-2 3C7 15 1 9 1 3z"/></svg>
        012-345-6789
      </li>
      <li>
        <svg viewBox="0 0 16 16" aria-hidden="true"><path d="M1 3h14v10H1z M1 3l7 6 7-6" fill="var(--ink)"/><path d="M2 4l6 5 6-5" fill="none" stroke="#fff" stroke-width="1.4"/></svg>
        info@youremail.com
      </li>
      <li>
        <svg viewBox="0 0 16 16" aria-hidden="true"><circle cx="8" cy="8" r="6.5" fill="none" stroke="var(--ink)" stroke-width="1.5"/><path d="M1.5 8h13M8 1.5c-3 3-3 10 0 13M8 1.5c3 3 3 10 0 13" fill="none" stroke="var(--ink)" stroke-width="1.2"/></svg>
        www.yourwebsite.com
      </li>
    </ul>
    <p class="address"><span class="address__label">Address</span>: Street name, Suite 100, State, Zip Code, Country</p>
  </section>
</main>
</body>
</html>
```